Corkmill Cafe' eLiquid Label - retro, trendy design

Need a 1.5"x3" label designed for an eLiquid bottle. I like the distressed retro diner look. Feel free to take creative license on logo, images etc. Attaching a mockup I did just to give you an idea of what look I want - the attached concept has all textual elements required....want retro trendy....hollowell-ish look and personality...warm colors...high contrasts. attached Vesk image is the mockup I want redesigned.

Target Market(s)

eclectic

Industry/Entity Type

Cafe

Font styles to use
Serif
Decorative

Requirements
Must have
• text elements from uploaded sample - 1.5x3 inch high res
Nice to have
• incorporate QN logo somewhere in the design - attached

```html
<!DOCTYPE html>
<html lang="en">
<head>
<meta charset="utf-8">
<title>Corkmill Vapor – Font Style Options</title>
<link rel="stylesheet" href="https://fonts.googleapis.com/css2?family=Oswald:wght@600&family=Ultra&family=Federo&family=Cinzel:wght@500;700&family=Cinzel+Decorative:wght@900&family=Limelight&family=Montserrat:wght@400;700&family=Anton&display=swap">
<style>
  :root {
    --canvas: #ffffff;
    --ink: #0b0b0b;
    --panel: #121212;
    --gold: #d6ad4c;
    --gold-light: #f1d98c;
    --gold-deep: #b98a2c;
    --cream: #f6edd3;
    --white: #ffffff;
    --magenta: #d10fb0;
  }
  * { box-sizing: border-box; margin: 0; padding: 0; }
  html, body { width: 1200px; height: 1000px; overflow: hidden; background: var(--canvas); }
  .board { position: relative; width: 1200px; height: 1000px; font-family: "Montserrat", sans-serif; }

  .board-title {
    position: absolute; left: 545px; top: 22px;
    font-family: "Anton", "Arial Black", sans-serif; font-size: 86px; letter-spacing: 4px;
    color: var(--magenta); line-height: 1;
  }

  .option-badge {
    position: absolute; width: 32px; height: 32px; border-radius: 50%;
    background: var(--magenta); border: 2px solid var(--ink);
    font: 700 19px/28px "Montserrat", sans-serif; color: var(--ink); text-align: center;
  }

  /* Header banners */
  .banner { position: absolute; left: 68px; width: 350px; background: var(--panel); border-top: 10px solid var(--gold); text-align: center; }
  .banner .option-badge { right: -10px; top: -14px; }
  .banner-brand { color: var(--gold); font-size: 38px; line-height: 1; margin-top: 26px; white-space: nowrap; }
  .banner-tagline { color: var(--white); font-size: 16px; margin-top: 6px; letter-spacing: .2px; }

  /* Bottle labels */
  .label { position: absolute; width: 295px; height: 252px; background: var(--panel); border-top: 7px solid var(--gold); text-align: center; overflow: hidden; }
  .label .option-badge { right: 40px; top: 58px; }
  .label-brand { color: var(--gold); font-size: 21px; line-height: 1; margin-top: 20px; white-space: nowrap; }
  .label-tagline { color: var(--white); font-size: 10px; margin-top: 3px; }
  .ornament-band {
    position: absolute; left: 18px; right: 18px; top: 100px; height: 48px;
    background: linear-gradient(90deg, transparent, var(--gold-deep) 20%, var(--gold) 50%, var(--gold-deep) 80%, transparent);
    opacity: .55; border-radius: 24px;
  }
  .emblem {
    position: absolute; left: 50%; top: 72px; width: 64px; height: 64px; margin-left: -32px;
    border-radius: 50%; background: var(--white);
    font: 700 22px/64px "Montserrat", sans-serif; color: var(--ink);
  }
  .label-flavor {
    position: absolute; left: 0; right: 0; top: 148px;
    font: 700 33px/1 "Cinzel", serif; color: var(--white); letter-spacing: 3px;
  }
  .label-rule { position: absolute; left: 40px; right: 40px; top: 188px; height: 1px; background: linear-gradient(90deg, transparent, var(--cream), transparent); }
  .label-strength { position: absolute; left: 0; right: 0; top: 196px; color: var(--white); font: 700 10px/1 "Montserrat", sans-serif; }
  .label-volume {
    position: absolute; left: 0; right: 0; bottom: 0; height: 30px;
    background: linear-gradient(90deg, var(--gold-deep), var(--cream) 35%, var(--cream) 65%, var(--gold-deep));
    font: 700 12px/30px "Montserrat", sans-serif; color: var(--ink);
  }
  .label-volume .star { color: var(--gold-deep); }

  /* Typeface options */
  .type-1 { font-family: "Oswald", sans-serif; font-weight: 600; }
  .type-2 { font-family: "Federo", serif; }
  .type-3 { font-family: "Cinzel Decorative", serif; font-weight: 900; letter-spacing: 1px; }
  .type-4 { font-family: "Limelight", serif; }
  .type-5 { font-family: "Ultra", serif; }
  .type-6 { font-family: "Cinzel", serif; font-weight: 500; }
  .banner .type-5, .banner .type-3 { font-size: 30px; margin-top: 30px; }
  .banner .type-6 { font-size: 32px; margin-top: 30px; }
  .label .type-5, .label .type-3 { font-size: 17px; }
</style>
</head>
<body>
<main class="board">
  <h1 class="board-title">FONT STYLE</h1>

  <section class="banner" style="top:42px;height:123px">
    <p class="banner-brand type-1">CORKMILL VAPOR</p>
    <p class="banner-tagline">ULTRA-PREMIUM MOD GREASE</p>
    <span class="option-badge">1</span>
  </section>
  <section class="banner" style="top:203px;height:117px">
    <p class="banner-brand type-5">CORKMILL VAPOR</p>
    <p class="banner-tagline">ULTRA-PREMIUM MOD GREASE</p>
    <span class="option-badge">5</span>
  </section>
  <section class="banner" style="top:366px;height:119px">
    <p class="banner-brand type-2">CORKMILL VAPOR</p>
    <p class="banner-tagline">ULTRA-PREMIUM MOD GREASE</p>
    <span class="option-badge">2</span>
  </section>
  <section class="banner" style="top:532px;height:118px">
    <p class="banner-brand type-6">CORKMILL VAPOR</p>
    <p class="banner-tagline">ULTRA-PREMIUM MOD GREASE</p>
    <span class="option-badge">6</span>
  </section>
  <section class="banner" style="top:683px;height:114px">
    <p class="banner-brand type-3">CORKMILL VAPOR</p>
    <p class="banner-tagline">ULTRA-PREMIUM MOD GREASE</p>
    <span class="option-badge">3</span>
  </section>
  <section class="banner" style="top:847px;height:115px">
    <p class="banner-brand type-4">CORKMILL VAPOR</p>
    <p class="banner-tagline">ULTRA-PREMIUM MOD GREASE</p>
    <span class="option-badge">4</span>
  </section>

  <article class="label" style="left:528px;top:138px">
    <p class="label-brand type-2">CORKMILL VAPOR</p>
    <p class="label-tagline">ULTRA-PREMIUM MOD GREASE</p>
    <div class="ornament-band" role="img" aria-label="Gold flourish scrollwork framing the emblem"></div>
    <div class="emblem">QN</div>
    <p class="label-flavor">VESKMISU</p>
    <div class="label-rule"></div>
    <p class="label-strength">12 mg Nicotine</p>
    <p class="label-volume">30 ml <span class="star">★</span> 70/30</p>
    <span class="option-badge">2</span>
  </article>
  <article class="label" style="left:861px;top:131px">
    <p class="label-brand type-5">CORKMILL VAPOR</p>
    <p class="label-tagline">ULTRA-PREMIUM MOD GREASE</p>
    <div class="ornament-band" role="img" aria-label="Gold flourish scrollwork framing the emblem"></div>
    <div class="emblem">QN</div>
    <p class="label-flavor">VESKMISU</p>
    <div class="label-rule"></div>
    <p class="label-strength">12 mg Nicotine</p>
    <p class="label-volume">30 ml <span class="star">★</span> 70/30</p>
    <span class="option-badge">5</span>
  </article>
  <article class="label" style="left:522px;top:427px">
    <p class="label-brand type-3">CORKMILL VAPOR</p>
    <p class="label-tagline">ULTRA-PREMIUM MOD GREASE</p>
    <div class="ornament-band" role="img" aria-label="Gold flourish scrollwork framing the emblem"></div>
    <div class="emblem">QN</div>
    <p class="label-flavor">VESKMISU</p>
    <div class="label-rule"></div>
    <p class="label-strength">12 mg Nicotine</p>
    <p class="label-volume">30 ml <span class="star">★</span> 70/30</p>
    <span class="option-badge">3</span>
  </article>
  <article class="label" style="left:849px;top:427px">
    <p class="label-brand type-4">CORKMILL VAPOR</p>
    <p class="label-tagline">ULTRA-PREMIUM MOD GREASE</p>
    <div class="ornament-band" role="img" aria-label="Gold flourish scrollwork framing the emblem"></div>
    <div class="emblem">QN</div>
    <p class="label-flavor">VESKMISU</p>
    <div class="label-rule"></div>
    <p class="label-strength">12 mg Nicotine</p>
    <p class="label-volume">30 ml <span class="star">★</span> 70/30</p>
    <span class="option-badge">4</span>
  </article>
  <article class="label" style="left:522px;top:708px">
    <p class="label-brand type-6">CORKMILL VAPOR</p>
    <p class="label-tagline">ULTRA-PREMIUM MOD GREASE</p>
    <div class="ornament-band" role="img" aria-label="Gold flourish scrollwork framing the emblem"></div>
    <div class="emblem">QN</div>
    <p class="label-flavor">VESKMISU</p>
    <div class="label-rule"></div>
    <p class="label-strength">12 mg Nicotine</p>
    <p class="label-volume">30 ml <span class="star">★</span> 70/30</p>
    <span class="option-badge">6</span>
  </article>
  <article class="label" style="left:855px;top:710px">
    <p class="label-brand type-1">CORKMILL VAPOR</p>
    <p class="label-tagline">ULTRA-PREMIUM MOD GREASE</p>
    <div class="ornament-band" role="img" aria-label="Gold flourish scrollwork framing the emblem"></div>
    <div class="emblem">QN</div>
    <p class="label-flavor">VESKMISU</p>
    <div class="label-rule"></div>
    <p class="label-strength">12 mg Nicotine</p>
    <p class="label-volume">30 ml <span class="star">★</span> 70/30</p>
    <span class="option-badge">1</span>
  </article>
</main>
</body>
</html>
```